morvel family medicine business cards

create business cards for 7 family medicine providers and 4 admin using attached logo
2 locations
appointment reminder on back of cards
will provide more info regarding names,addresses, credentials etc once started

```html
<!DOCTYPE html>
<html lang="en">
<head>
<meta charset="utf-8">
<title>Morvel Family Medicine Business Cards</title>
<link rel="stylesheet" href="https://fonts.googleapis.com/css2?family=Open+Sans:wght@400;600;700&display=swap">
<style>
  :root {
    --backdrop: #808080;
    --card: #ffffff;
    --navy: #231f5c;
    --sky: #29a8e0;
    --grey-text: #555555;
    --divider: #9a9a9a;
  }
  * { margin: 0; padding: 0; box-sizing: border-box; }
  html, body { width: 1200px; height: 1000px; overflow: hidden; }
  body {
    background: var(--backdrop);
    font-family: "Open Sans", Arial, sans-serif;
    position: relative;
  }
  .card {
    position: absolute;
    width: 612px;
    height: 351px;
    background: var(--card);
    border-radius: 30px;
    box-shadow: 0 8px 22px rgba(0,0,0,0.35);
  }
  .card--front { left: 295px; top: 120px; }
  .card--back { left: 294px; top: 528px; }
  .divider {
    position: absolute;
    left: 306px;
    width: 1px;
    background: var(--divider);
  }
  .card--front .divider { top: 65px; height: 222px; }
  .card--back .divider { top: 65px; height: 222px; }

  .brand {
    position: absolute;
    display: flex;
    align-items: center;
    justify-content: center;
    color: var(--navy);
    font-weight: 700;
  }
  .brand__dot { border-radius: 50%; background: var(--sky); flex: none; }
  .card--front .brand { left: 50px; top: 48px; width: 225px; height: 50px; font-size: 17px; gap: 8px; }
  .card--front .brand__dot { width: 30px; height: 30px; }
  .card--back .brand {
    left: 40px; top: 80px; width: 250px; height: 180px;
    flex-direction: column; gap: 14px; font-size: 24px; text-align: center; line-height: 1.15;
  }
  .card--back .brand__dot { width: 96px; height: 96px; }

  .staff {
    position: absolute;
    left: 30px; top: 115px; width: 265px;
    list-style: none;
    text-align: center;
    color: var(--sky);
    font-weight: 600;
    font-size: 15.5px;
    line-height: 19.3px;
  }

  .contact {
    position: absolute;
    left: 320px; top: 64px; width: 256px;
    text-align: center;
    font-size: 12px;
    line-height: 14.4px;
    color: var(--grey-text);
  }
  .location { margin-bottom: 9px; }
  .pin { display: block; margin: 0 auto 5px; }
  .location__title, .phone, .web { color: var(--navy); font-weight: 700; }
  .icons { display: flex; justify-content: center; gap: 4px; margin: 4px 0 3px; }

  .reminder {
    position: absolute;
    left: 322px; top: 102px; width: 260px;
    color: var(--navy);
    font-size: 12px;
  }
  .reminder__lead { text-align: center; margin-bottom: 30px; }
  .field { display: flex; align-items: flex-end; font-weight: 700; margin-bottom: 7px; }
  .field__line { border-bottom: 1px solid var(--navy); height: 14px; margin-left: 5px; position: relative; }
  .field__line--name { width: 207px; }
  .field__line--date { width: 120px; margin-left: 5px; font-weight: 400; }
  .field__line--time { width: 48px; }
  .slash { position: absolute; top: -3px; }
  .reminder__note { text-align: center; margin-top: 24px; line-height: 15px; }
</style>
</head>
<body>

<section class="card card--front">
  <div class="brand">
    <span class="brand__dot"></span>
    <span>Morvel Family Medicine</span>
  </div>
  <ul class="staff">
    <li>Dr. Tobin Morvel</li>
    <li>Dr. Karina Morvel</li>
    <li>Dr. Wanda Cresley</li>
    <li>Marissa Dalloway</li>
    <li>Dr. Alessandra Thornquist</li>
    <li>Carolyn Whitfield</li>
    <li>Jessa Romero</li>
    <li>Joel Brandt</li>
    <li>Liliana Fontaine-Ocampo</li>
  </ul>
  <div class="divider"></div>
  <div class="contact">
    <div class="location">
      <svg class="pin" width="11" height="15" viewBox="0 0 11 15"><path d="M5.5 0C2.5 0 0 2.4 0 5.4 0 9.3 5.5 15 5.5 15S11 9.3 11 5.4C11 2.4 8.5 0 5.5 0z" fill="#29a8e0"/><circle cx="5.5" cy="5.4" r="2" fill="#fff"/></svg>
      <div class="location__title">BROOKFIELD LOCATION</div>
      <div>4218 Harbor Point Road, Suite 310</div>
      <div>Brookfield, Florida 33021</div>
      <div class="phone">(555) 214-3870</div>
    </div>
    <div class="location">
      <svg class="pin" width="11" height="15" viewBox="0 0 11 15"><path d="M5.5 0C2.5 0 0 2.4 0 5.4 0 9.3 5.5 15 5.5 15S11 9.3 11 5.4C11 2.4 8.5 0 5.5 0z" fill="#29a8e0"/><circle cx="5.5" cy="5.4" r="2" fill="#fff"/></svg>
      <div class="location__title">LAKEVIEW LOCATION</div>
      <div>1750 W. Meridian Parkway, Suite 105</div>
      <div>Lakeview, Florida 33029</div>
      <div class="phone">(555) 362-4491</div>
    </div>
    <div class="icons">
      <svg width="14" height="10" viewBox="0 0 14 10"><rect x="0.5" y="0.5" width="13" height="9" fill="#29a8e0"/><path d="M0.5 0.5 7 5.5 13.5 0.5" fill="none" stroke="#fff" stroke-width="1"/></svg>
      <svg width="11" height="11" viewBox="0 0 11 11"><circle cx="5.5" cy="5.5" r="5" fill="none" stroke="#29a8e0" stroke-width="1"/><ellipse cx="5.5" cy="5.5" rx="2.2" ry="5" fill="none" stroke="#29a8e0" stroke-width="1"/><path d="M0.5 5.5h10M1.3 3h8.4M1.3 8h8.4" stroke="#29a8e0" stroke-width="1"/></svg>
    </div>
    <div class="web">office@morvelclinic.com</div>
    <div class="web">morvelclinic.com</div>
  </div>
</section>

<section class="card card--back">
  <div class="brand">
    <span class="brand__dot"></span>
    <span>Morvel Family Medicine</span>
  </div>
  <div class="divider"></div>
  <div class="reminder">
    <p class="reminder__lead">Your next appointment is schedule for:</p>
    <div class="field">Name: <span class="field__line field__line--name"></span></div>
    <div class="field">
      <span style="margin-left:7px">Date:</span>
      <span class="field__line field__line--date"><span class="slash" style="left:43px">/</span><span class="slash" style="left:69px">/</span></span>
      <span style="margin-left:3px">Time:</span>
      <span class="field__line field__line--time"></span>
    </div>
    <p class="reminder__note">Please give 24 hours notice for cancellations<br>to avoid a $50,00 no show fee.</p>
  </div>
</section>

</body>
</html>
```